RM Tomás Rivera (Business Card)

Hi designers, in this work, I'm looking for an sophisticated stylish, elegant and proffesional personal card. We have a laboratory of pathology automated, with equipments high quality.
In this web the designers, have created my business logo, the name is "RM Tomás Rivera"
In our lab, we principal work is to prepare the biopsies for further diagnostic of diseases like cancer, tumors, etc.
I need that the first face, only having my complete logo (Rm Tomás Rivera, Laboratorio de procesamiento Histologico)
The overleaf, could repeat the same logo, like water logo.
In this face, I need to say: My full data:

Técnico en Anatomía Patológica
Tomás Rivera Ibarra M.P 47203
Av. Paredes Luján 418 - 2do piso - Instituto Marbel.
Córdoba, Argentina
(0351) 154820937
rivera.tomas@correolab.example

with respect the colors of card, use your imagination, the original logo color is violet, I haven't chosen a color base for the card.

attached pictures are examples of cards I like your DESIGN.
Attached too, the original logo to my company.

the size of card are:
horizontal: 9cm
vertical: 5,5cm

any question that you have, not doubt to question me,
Hand to work!

Industry/Entity Type

Laboratory

Requirements
Must have
• designers sophisticated, not simples, like show the images attached

```html
<!DOCTYPE html>
<html lang="es">
<head>
<meta charset="utf-8">
<title>Tomás Rivera – Tarjeta personal</title>
<link rel="stylesheet" href="https://fonts.googleapis.com/css2?family=Roboto+Condensed:ital,wght@0,300;0,400;0,700;1,300;1,700&display=swap">
<style>
  :root {
    --page-bg: #ece9ef;
    --violet-light: #a046cf;
    --violet: #8a36bf;
    --violet-deep: #6a1fa0;
    --ink-light: #ffffff;
    --ink-soft: rgba(255,255,255,0.82);
    --card-shadow: rgba(60, 20, 90, 0.28);
  }
  * { margin: 0; padding: 0; box-sizing: border-box; }
  html, body {
    width: 1200px; height: 1023px; overflow: hidden;
    background: var(--page-bg);
    font-family: "Roboto Condensed", Arial, sans-serif;
  }
  .sheet {
    width: 1200px; height: 1023px;
    display: flex; flex-direction: column; align-items: center; justify-content: center;
    gap: 35px;
  }
  .card {
    position: relative;
    width: 760px; height: 464px;
    border-radius: 22px;
    background: radial-gradient(ellipse at 55% 35%, var(--violet-light) 0%, var(--violet) 45%, var(--violet-deep) 100%);
    box-shadow: 0 14px 34px var(--card-shadow);
    color: var(--ink-light);
    overflow: hidden;
  }

  /* Front: brand lockup */
  .card-front { display: flex; align-items: center; justify-content: center; }
  .brand { display: flex; flex-direction: column; align-items: center; }
  .brand-row { display: flex; align-items: center; gap: 16px; }
  .brand-mark {
    width: 16px; height: 16px; border-radius: 50%;
    background: var(--ink-light);
  }
  .brand-name {
    font-weight: 300; font-size: 30px; letter-spacing: 0.42em;
    text-transform: uppercase;
  }
  .brand-tagline {
    margin-top: 12px;
    font-weight: 400; font-size: 25px; letter-spacing: 0.01em;
    text-transform: uppercase;
  }

  /* Back: contact data */
  .card-back { padding: 70px 80px; display: flex; flex-direction: column; justify-content: center; }
  .holder-name {
    font-weight: 700; font-style: italic; font-size: 34px; letter-spacing: 0.01em;
  }
  .holder-title {
    margin-top: 4px;
    font-weight: 300; font-style: italic; font-size: 22px; color: var(--ink-soft);
  }
  .contact { margin-top: 34px; list-style: none; }
  .contact li {
    display: flex; align-items: center; gap: 12px;
    font-weight: 300; font-size: 21px; line-height: 1.55; color: var(--ink-soft);
  }
  .contact svg { width: 18px; height: 18px; flex: none; fill: none; stroke: var(--ink-light); stroke-width: 1.8; }
</style>
</head>
<body>
<main class="sheet">
  <section class="card card-front" aria-label="Frente de la tarjeta">
    <div class="brand">
      <div class="brand-row">
        <span class="brand-mark" aria-hidden="true"></span>
        <span class="brand-name">Tomás Rivera</span>
      </div>
      <div class="brand-tagline">Laboratorio de procesamiento histológico</div>
    </div>
  </section>

  <section class="card card-back" aria-label="Dorso de la tarjeta">
    <h1 class="holder-name">Tomás Rivera Ibarra M.P 47203</h1>
    <p class="holder-title">Técnico en Anatomía Patológica</p>
    <ul class="contact">
      <li>
        <svg viewBox="0 0 24 24" aria-hidden="true"><path d="M12 22s7-7.2 7-12.5A7 7 0 0 0 5 9.5C5 14.8 12 22 12 22z"/><circle cx="12" cy="9.5" r="2.5"/></svg>
        Av. Paredes Luján 418 - 2do piso - Instituto Marbel. Córdoba, Argentina
      </li>
      <li>
        <svg viewBox="0 0 24 24" aria-hidden="true"><path d="M5 3h4l2 5-2.5 1.5a11 11 0 0 0 6 6L16 13l5 2v4a2 2 0 0 1-2 2A16 16 0 0 1 3 5a2 2 0 0 1 2-2z"/></svg>
        (0351) 154820937
      </li>
      <li>
        <svg viewBox="0 0 24 24" aria-hidden="true"><rect x="3" y="5" width="18" height="14" rx="2"/><path d="M3 7l9 6 9-6"/></svg>
        rivera.tomas@correolab.example
      </li>
    </ul>
  </section>
</main>
</body>
</html>
```